PEDAL ROAST With Cycling Theme Wants Business Cards

We want to create a business card for a PEDAL ROAST that has a cycling theme. We expect to use the current logo on one side of the business card and we have been considering adding the words 'PEDAL ROAST' underneath (see example). For the other side of the business card we want an interesting design with tag-line, address and social media links (the normal business card stuff). See examples provided but we are not fixed on having it exactly as shown, we are very open to great creative ideas. Please note our logo has the initials ‘RM' in orange embedded in the design and this must be retained. However, you can play with the words PEDAL ROAST as well as use the orange color on the backside of the business card, as you see fit. For an image on the backside of the business card it can be a photo, hand-drawn or whatever but it must visually combine brewed for riders in some way. The interior of the PEDAL ROAST will be reclaimed wood, rustic and have an urban feel to it with cycling artifacts hanging from the walls/ceiling, etc. Finally, it would be beneficial if the business card design elements can be easily used on flyers and other promotional assets. Good luck, we are looking forward to seeing your creative ideas.

Target Market(s)

Coffee lovers and cycling fans

Contact Information for Business Card

See project description.

Colors

Designer to choose colors to be used in the design.

Requirements
Must have
• Must use the current logo provided and combine a coffee and bike theme.
Nice to have
• Orange is used in current logo and could be used as an accent color on the backside of the business card.

```html
<!DOCTYPE html>
<html lang="en">
<head>
<meta charset="utf-8">
<title>Pedal Roast – Business Cards</title>
<link rel="stylesheet" href="https://fonts.googleapis.com/css2?family=Oswald:wght@500;700&family=Roboto:ital,wght@0,400;1,500&display=swap">
<style>
  :root {
    --stage: #1f1f1f;
    --card: #fbfaf8;
    --bean-tone: #efebe6;
    --orange: #ff6a21;
    --ink: #1b1b1b;
    --grey: #555555;
    --rule: #9a9a9a;
    --white: #ffffff;
  }
  * { margin: 0; padding: 0; box-sizing: border-box; }
  html, body { width: 1125px; height: 1200px; overflow: hidden; }
  body {
    background: var(--stage);
    position: relative;
    font-family: "Roboto", Arial, sans-serif;
  }
  .card {
    position: absolute;
    left: 147px;
    width: 825px;
    height: 472px;
    background: var(--card);
    overflow: hidden;
  }
  .card--front { top: 102px; }
  .card--back { top: 635px; }

  .bean-pattern {
    position: absolute;
    inset: 0;
    background: radial-gradient(ellipse at center, var(--card) 0%, var(--bean-tone) 130%);
  }

  /* Front */
  .identity {
    position: absolute;
    right: 455px;
    top: 192px;
    text-align: right;
  }
  .identity__name {
    font-family: "Oswald", "Arial Narrow", sans-serif;
    font-weight: 500;
    font-size: 37px;
    line-height: 1;
    color: var(--orange);
  }
  .identity__role {
    font-size: 21px;
    color: var(--ink);
    margin-top: 4px;
  }
  .divider {
    position: absolute;
    left: 397px;
    top: 170px;
    width: 1px;
    height: 130px;
    background: var(--rule);
  }
  .contacts {
    position: absolute;
    left: 424px;
    top: 170px;
    list-style: none;
  }
  .contacts__item {
    display: flex;
    align-items: center;
    height: 26.3px;
    font-size: 19.5px;
    color: var(--grey);
  }
  .contacts__icon {
    width: 18px;
    height: 18px;
    margin-right: 14px;
    fill: var(--orange);
  }
  .address-band {
    position: absolute;
    left: 0;
    right: 0;
    top: 397px;
    height: 40px;
    background: var(--orange);
    display: flex;
    align-items: center;
    justify-content: center;
    color: var(--white);
    font-size: 19.5px;
  }
  .address-band__pin {
    width: 18px;
    height: 22px;
    margin-right: 12px;
    fill: var(--white);
  }

  /* Back */
  .brand {
    position: absolute;
    left: 0;
    right: 0;
    top: 84px;
    text-align: center;
  }
  .brand__mark {
    display: inline-flex;
    align-items: center;
    gap: 18px;
    height: 150px;
  }
  .brand__dot {
    width: 34px;
    height: 34px;
    border-radius: 50%;
    background: var(--orange);
  }
  .brand__initials {
    font-family: "Oswald", "Arial Narrow", sans-serif;
    font-weight: 700;
    font-size: 120px;
    line-height: 1;
    color: var(--orange);
  }
  .brand__name {
    font-family: "Oswald", "Arial Narrow", sans-serif;
    font-weight: 700;
    font-size: 40px;
    line-height: 1;
    color: var(--orange);
    letter-spacing: 1px;
    margin-top: 14px;
  }
  .brand__tagline {
    font-style: italic;
    font-weight: 500;
    font-size: 27px;
    color: var(--grey);
    margin-top: 2px;
  }
  .brand__social {
    font-size: 19px;
    color: var(--grey);
    margin-top: 8px;
  }
</style>
</head>
<body>

<section class="card card--front">
  <div class="bean-pattern" role="img" aria-label="Faint scattered coffee bean pattern background"></div>

  <div class="identity">
    <h1 class="identity__name">DANA REYES</h1>
    <p class="identity__role">CEO/FOUNDER</p>
  </div>

  <div class="divider"></div>

  <ul class="contacts">
    <li class="contacts__item">
      <svg class="contacts__icon" viewBox="0 0 24 24"><path d="M6.6 10.8a15.2 15.2 0 0 0 6.6 6.6l2.2-2.2c.3-.3.7-.4 1-.2 1.1.4 2.3.6 3.6.6.6 0 1 .4 1 1V20c0 .6-.4 1-1 1A17 17 0 0 1 3 4c0-.6.4-1 1-1h3.5c.6 0 1 .4 1 1 0 1.300.2 2.500.6 3.600.1.3 0 .7-.2 1z"/></svg>
      555 210 4817
    </li>
    <li class="contacts__item">
      <svg class="contacts__icon" viewBox="0 0 24 24"><path d="M7 1h10a2 2 0 0 1 2 2v18a2 2 0 0 1-2 2H7a2 2 0 0 1-2-2V3a2 2 0 0 1 2-2zm0 3v14h10V4zm5 15.5a1.2 1.2 0 1 0 0 2.4 1.2 1.2 0 0 0 0-2.4z"/></svg>
      555 314 7702
    </li>
    <li class="contacts__item">
      <svg class="contacts__icon" viewBox="0 0 24 24"><path d="M6 2h12v6H6zM3 9h18a2 2 0 0 1 2 2v7h-4v4H5v-4H1v-7a2 2 0 0 1 2-2zm4 7v4h10v-4z"/></svg>
      555 468 2093
    </li>
    <li class="contacts__item">
      <svg class="contacts__icon" viewBox="0 0 24 24"><path d="M2 5h20v14H2zm2 2v.5l8 5.5 8-5.5V7z"/></svg>
      hello@pedalroast.cafe
    </li>
    <li class="contacts__item">
      <svg class="contacts__icon" viewBox="0 0 24 24"><path d="M12 2a10 10 0 1 0 0 20 10 10 0 0 0 0-20zm-1 17.9A8 8 0 0 1 4.2 10l4.8 4.8v1a2 2 0 0 0 2 2zm6.9-2.5A2 2 0 0 0 16 16h-1v-3a1 1 0 0 0-1-1H8v-2h2a1 1 0 0 0 1-1V7h2a2 2 0 0 0 2-2v-.4a8 8 0 0 1 2.9 12.8z"/></svg>
      www.pedalroast.cafe
    </li>
  </ul>

  <div class="address-band">
    <svg class="address-band__pin" viewBox="0 0 24 30"><path d="M12 0A10 10 0 0 0 2 10c0 7.5 10 20 10 20s10-12.5 10-20A10 10 0 0 0 12 0zm0 14a4 4 0 1 1 0-8 4 4 0 0 1 0 8z"/></svg>
    1420 Alder Street, Juneau, Alaska 99801
  </div>
</section>

<section class="card card--back">
  <div class="bean-pattern" role="img" aria-label="Faint scattered coffee bean pattern background"></div>

  <div class="brand">
    <div class="brand__mark">
      <span class="brand__dot"></span>
      <span class="brand__initials">RM</span>
    </div>
    <h2 class="brand__name">PEDAL ROAST</h2>
    <p class="brand__tagline">brewed for riders</p>
    <p class="brand__social">@pedalroast</p>
  </div>
</section>

</body>
</html>
```